Gadgetpickerhelp.com needs your creativity!

We need a website design for a new internet company based in Winnipeg MB called gadgetpickerhelp.com. We provide customers who are relatively new to technology a professional intermediary in the computer buying process. We act as an independent purchasing assistant for our customers by getting a clear understanding of their needs and requirements of their machine and proceed to find a computer with the exact specifications they require at the lowest possible price. Because we are completely independent we do not push any particular brand, OS, or software. We want the website to be bold but streamlined, it should be easy to use and navigate even for a beginner.

Target Market(s)

45+ age bracket

Industry/Entity Type

Internet

Requirements
Must have
• The site must have an About Us page, as well as a secure shopping cart where customers can purchase the service via paylinko and credit card. In this section we will require all of the customer's information to be entered as well as what their needs are for their new computer
I would like a product comparison chart that is broken down into three columns where the features of each service can be checked or unchecked depending on each package. I also need an extended service page, where customers will be able to contact me or directly purchase a remote servicing package
Nice to have
• I would like to have an introductory video for the service provided available to customers on the home page so one click and they will be able to see what our service is about.
Should not have
• Do not use any loud audio or sound clips in the design, subtle sound is fine.

```html
<!DOCTYPE html>
<html lang="en">
<head>
<meta charset="utf-8">
<title>Gadget Picker Help</title>
<link rel="stylesheet" href="https://fonts.googleapis.com/css2?family=Arimo:wght@400;700&family=Roboto:wght@300;400;500&family=Tinos&display=swap">
<style>
:root{
  --green:#5a8a16;
  --green-dark:#3f6a0c;
  --green-deep:#34410f;
  --olive-text:#3d5a0a;
  --ink:#333;
  --muted:#555;
  --line:#dcdcdc;
  --panel:#f3f3f3;
  --price:#b8170e;
  --white:#fff;
}
*{box-sizing:border-box;margin:0;padding:0}
html,body{width:946px;height:1200px;overflow:hidden}
body{position:relative;background:#fafafa;font-family:Arimo,Arial,sans-serif;color:var(--ink)}
.abs{position:absolute}
.header{left:0;top:0;width:946px;height:132px;background:linear-gradient(180deg,#6b9a1f,#5a8a16 60%,#52800f);border-bottom:4px solid #e8e8e8}
.brand{left:34px;top:40px;display:flex;align-items:center;gap:12px;color:var(--white)}
.brand-mark{width:24px;height:24px;background:var(--white)}
.brand-name{font-family:Tinos,serif;font-size:27px;letter-spacing:.5px}
.toplinks{left:488px;top:31px;color:var(--white);font-size:11.5px;font-family:Roboto,sans-serif}
.toplinks span{margin:0 4px}
.search{left:763px;top:26px;width:170px;height:22px;background:var(--white);border:1px solid #ccc;border-radius:2px;font-size:9.5px;color:#aaa;font-style:italic;padding:5px 12px}
.search svg{position:absolute;right:6px;top:5px}
.nav{left:494px;top:76px;height:36px;display:flex;background:linear-gradient(#4a4a4a,#222);border-radius:2px;box-shadow:0 1px 2px rgba(0,0,0,.4)}
.nav a{color:var(--white);text-decoration:none;font-family:Roboto,sans-serif;font-size:12.5px;display:flex;align-items:center;justify-content:center;border-left:1px solid #555}
.nav a.on{background:#0c0c0c;border-left:0}
.slider{left:32px;top:152px;width:618px;height:295px;background:linear-gradient(90deg,#fff,#ececec);box-shadow:0 6px 8px -6px rgba(0,0,0,.35)}
.slide-art{left:20px;top:20px;width:380px;height:265px;background:linear-gradient(135deg,#333 0%,#8a1820 40%,#cfe2ee 60%,#222 100%);opacity:.85;border-radius:4px}
.offer{left:409px;top:158px;font-family:Roboto,sans-serif;color:var(--olive-text);font-size:22px;font-weight:300}
.click{left:446px;top:224px;font-family:Roboto,sans-serif;color:var(--olive-text);font-size:17px;font-weight:300}
.arrow{top:124px;width:20px;height:38px;background:#1a1a1a;display:flex;align-items:center;justify-content:center}
.cats{left:673px;top:151px;width:231px;height:296px;background:linear-gradient(#fff,#eee);border:1px solid var(--line);border-radius:3px}
.cats h3{position:absolute;left:46px;top:19px;font:400 13px Roboto,sans-serif;color:var(--green)}
.cats ul{list-style:none;position:absolute;left:30px;top:50px}
.cats li{font:400 12.5px Roboto,sans-serif;color:#444;height:32.5px}
.cats li::before{content:"›";color:#888;margin-right:10px}
.cats .more{position:absolute;right:17px;bottom:22px;font-size:9.5px;color:var(--green)}
.rule{left:0;width:946px;height:1px;background:var(--line)}
.welcome h2{position:absolute;left:34px;top:490px;font:400 17px Roboto,sans-serif;color:#555}
.welcome h2 b{font-weight:400;color:var(--olive-text)}
.intro{left:33px;top:525px;width:560px;font-size:11.3px;line-height:14.4px;color:#444}
.intro p{margin-bottom:14.4px}
.video{left:598px;top:519px;width:319px;height:196px;border:10px solid #000;background:linear-gradient(135deg,#fff,#e0e6ea 55%,#6ab0e6)}
.play{left:138px;top:69px}
.box{background:var(--panel);border-radius:3px}
.box-title{font:400 16px Roboto,sans-serif;color:var(--olive-text);display:flex;align-items:center;gap:10px}
.icon-dot{width:22px;height:22px;background:#c9862c;border-radius:50%}
.field{width:161px;height:21px;background:var(--white);border:1px solid #ccc;border-radius:3px;font-size:10px;padding:5px 12px;color:#333}
.submit{width:89px;height:29px;background:linear-gradient(#333,#000);color:var(--white);font:400 12px Roboto,sans-serif;display:flex;align-items:center;justify-content:center;border-radius:2px}
.cart-text{font-size:10.8px;line-height:19px;color:#444}
.feat-tab{left:276px;top:768px;width:240px;height:35px;background:linear-gradient(#5e8b18,#44700b);color:var(--white);font:400 16px Roboto,sans-serif;padding:8px 20px;border-radius:2px 2px 0 0}
.feat-line{left:276px;top:802px;width:629px;height:1px;background:#ccc}
.feat-panel{left:276px;top:803px;width:629px;height:272px;background:linear-gradient(#fff,#f0f0f0);border:1px solid #ddd;border-top:0}
.circ{top:773px;width:25px;height:25px;border-radius:50%;background:#111;display:flex;align-items:center;justify-content:center}
.product{width:163px;top:838px}
.thumb{width:163px;height:105px;background:var(--white);border:1px solid #ddd;border-radius:3px;display:flex;align-items:center;justify-content:center}
.thumb div{width:110px;height:70px;border-radius:3px}
.pdesc{margin-top:12px;font-size:9.6px;line-height:16px;color:#444;padding-left:5px;white-space:nowrap}
.pbuy{margin-top:8px;display:flex;align-items:center;justify-content:space-between;padding-left:11px}
.price{color:var(--price);font-size:12px}
.add{width:86px;height:26px;background:linear-gradient(#4e7a12,#2f4e06);color:var(--white);font:400 12px Roboto,sans-serif;display:flex;align-items:center;justify-content:center;border-radius:3px;margin-right:-1px}
.footer{left:0;top:1121px;width:946px;height:79px;background:var(--green-deep);border-top:3px solid var(--green-dark)}
.pay{left:44px;top:11px;display:flex;gap:5px;align-items:center}
.card{width:35px;height:20px;background:#e8e8e8;font-size:6.5px;color:#333;display:flex;align-items:center;justify-content:center}
.payname{color:var(--white);font:700 15px Arimo,sans-serif;margin-left:4px}
.social{left:46px;top:49px;display:flex;gap:16px}
.social div{width:20px;height:20px;background:#7a8a9c;border-radius:2px}
.copy{right:40px;top:19px;color:var(--white);font-size:9.5px}
.x2{right:40px;top:52px;color:var(--white);font-size:11.5px}
</style>
</head>
<body>
<header class="abs header">
  <div class="abs brand"><div class="brand-mark"></div><div class="brand-name">GADGET PICKER HELP</div></div>
  <div class="abs toplinks">(0) Items <span></span>Login <span>|</span> Create an account <span>|</span> My Cart</div>
  <div class="abs search">Search Product
    <svg width="10" height="10" viewBox="0 0 10 10"><circle cx="4" cy="4" r="3" fill="none" stroke="#aaa"/><line x1="6" y1="6" x2="9" y2="9" stroke="#aaa"/></svg>
  </div>
  <nav class="abs nav">
    <a class="on" style="width:72px">Home</a>
    <a style="width:99px">About Us</a>
    <a style="width:80px">FAQ's</a>
    <a style="width:89px">Sign Up</a>
    <a style="width:98px">Contact Us</a>
  </nav>
</header>

<section class="abs slider">
  <div class="abs slide-art" role="img" aria-label="Three open laptops in black and red"></div>
  <div class="abs offer">Special Offers</div>
  <div class="abs click">» Click Here</div>
  <div class="abs arrow" style="left:1px"><svg width="6" height="8"><path d="M4 1L1 4l3 3" stroke="#fff" fill="none"/></svg></div>
  <div class="abs arrow" style="left:598px"><svg width="6" height="8"><path d="M2 1l3 3-3 3" stroke="#fff" fill="none"/></svg></div>
</section>

<aside class="abs cats">
  <svg class="abs" style="left:24px;top:20px" width="16" height="16"><circle cx="8" cy="8" r="7" fill="#fff" stroke="#ccc"/><path d="M7 5l3 3-3 3" stroke="#888" fill="none"/></svg>
  <h3>CATEGORIES</h3>
  <ul>
    <li>Customer Testimonials</li>
    <li>Computer Accessories</li>
    <li>Veltrix</li>
    <li>Norvane</li>
    <li>Sprayline</li>
    <li>Crestmark</li>
  </ul>
  <div class="more">More &nbsp;&gt;&gt;</div>
</aside>

<div class="abs rule" style="top:470px"></div>

<section class="welcome">
  <h2>Welcome to <b>Gadget Picker Help</b></h2>
  <div class="abs intro">
    <p>Currently the computer buying market offers two distinct, yet underwhelming choices;</p>
    <p>A: Greatly overpay for a unique and different operating system than you are used to and be left to deal with the numerous challenges of adapting to the new platform</p>
    <p>B: Pay less for a computer you have been told is great by the green sales associate, only to discover the machine does not meet,or is way above your needs.</p>
    <p>Now you have a real alternative, a professional in the industry working solely for YOU.</p>
    <p>So why choose Gadget Picker Help? It will save you time and money in the long run! The computer will be purchased at the lowest price and delivered to your door with the full manufacturer's warranty. Because the hardware specifications will be of the highest quality and with our simple remote service offerings the computer will give you many more years of productive use.</p>
  </div>
  <div class="abs video" role="img" aria-label="Introductory video showing an open laptop">
    <svg class="abs play" width="40" height="30"><rect width="40" height="30" rx="5" fill="#111"/><path d="M15 8l12 7-12 7z" fill="#fff"/></svg>
  </div>
</section>

<div class="abs rule" style="top:752px"></div>

<section class="abs box" style="left:31px;top:770px;width:227px;height:160px">
  <div class="abs box-title" style="left:12px;top:8px"><div class="icon-dot"></div>Login</div>
  <div class="abs field" style="left:24px;top:54px">User Name</div>
  <div class="abs field" style="left:24px;top:85px">Password</div>
  <div class="abs submit" style="left:27px;top:122px">Submit</div>
</section>

<section class="abs box" style="left:31px;top:945px;width:227px;height:158px">
  <div class="abs box-title" style="left:12px;top:6px"><div class="icon-dot" style="background:#5a8a16"></div>Your Shopping Cart</div>
  <div class="abs cart-text" style="left:10px;top:50px;width:210px">Contains 0 Items<br>Welcome to your alternative to computer shopping. Are you overwhelmed, confused or under-informed as to the type and of computer you should buy?</div>
</section>

<div class="abs feat-panel"></div>
<div class="abs feat-line"></div>
<div class="abs feat-tab">Featured</div>
<div class="abs circ" style="left:843px"><svg width="6" height="8"><path d="M4 1L1 4l3 3" stroke="#fff" fill="none"/></svg></div>
<div class="abs circ" style="left:874px"><svg width="6" height="8"><path d="M2 1l3 3-3 3" stroke="#fff" fill="none"/></svg></div>

<div class="abs product" style="left:290px">
  <div class="thumb"><div role="img" aria-label="Laptop with a purple screen" style="background:linear-gradient(135deg,#ddd,#8a2a8a 50%,#ccc)"></div></div>
  <div class="pdesc">Uenim ad minim veniam, quis nostrud<br>laboris nisi utaliquip ex irurdolor into</div>
  <div class="pbuy"><span class="price">$300.00</span><span class="add">Add To Cart</span></div>
</div>
<div class="abs product" style="left:498px">
  <div class="thumb"><div role="img" aria-label="Desktop computer with green screen" style="background:linear-gradient(135deg,#4a8a1a,#222 55%,#bbb)"></div></div>
  <div class="pdesc">Uenim ad minim veniam, quis nostrud<br>laboris nisi utaliquip ex irurdolor into</div>
  <div class="pbuy"><span class="price">$300.00</span><span class="add">Add To Cart</span></div>
</div>
<div class="abs product" style="left:715px">
  <div class="thumb"><div role="img" aria-label="Desktop tower with monitor and keyboard" style="background:linear-gradient(135deg,#222,#6aa0d8 50%,#ccc)"></div></div>
  <div class="pdesc">Uenim ad minim veniam, quis nostrud<br>laboris nisi utaliquip ex irurdolor into</div>
  <div class="pbuy"><span class="price">$300.00</span><span class="add">Add To Cart</span></div>
</div>

<footer class="abs footer">
  <div class="abs pay">
    <div class="card">Cardora</div><div class="card">Mintcard</div><div class="card">Amberpay</div><div class="card">Nexa</div>
    <span class="payname">Paylinko</span>
  </div>
  <div class="abs social"><div></div><div></div><div></div><div></div><div></div></div>
  <div class="abs copy">© 2012 Gadgetpickerhelp, All rights reserved</div>
  <div class="abs x2">x2</div>
</footer>
</body>
</html>
```